Tolbrook Dental Surgery Business Cards

Hi there

Can i please have a simple business card designed (front and back with a black background) using out white reverse logo and the same font used for the logo?
On the back we can just have the logo. Full details at the front part.
Here are the details:

Name of the surgery: Tolbrook | Dental Surgery
Name on the business card: Dr Marek Ostby
Credentials:
BDSc (KRT)
MSc Oral Implantology (Lindqvist, Frankfurt)
Fellow & Diplomate (Meridian Society of Jaw Restoration)

Email: marek.ostby@tolbrookdental.com.au
Address: 17 Wexcombe Rd Ellendale
Website: tolbrookdental.com.au
Phone: 1800 357 218

We have attached our high res logo and a rudimentary version of the business card which is not necessarily what we want but gives all the details
We would like to have the print ready version. Thanks.

Contact Information for Business Card

website. credentials. qr code. address. phone number

Requirements
Must have
• QR code

```html
<!DOCTYPE html>
<html lang="en">
<head>
<meta charset="utf-8">
<title>Tolbrook Dental Surgery – Business Cards</title>
<link rel="stylesheet" href="https://fonts.googleapis.com/css2?family=Montserrat:wght@400;500;600;700&display=swap">
<style>
  :root {
    --backdrop: #1b1b1b;
    --card: #141414;
    --card-edge: #262626;
    --ink: #ffffff;
    --ink-soft: #e6e6e6;
    --emboss: #3b3b3b;
  }
  * { box-sizing: border-box; margin: 0; padding: 0; }
  html, body {
    width: 900px; height: 1200px; overflow: hidden;
    background: var(--backdrop);
    font-family: "Montserrat", sans-serif;
  }
  .canvas { position: relative; width: 900px; height: 1200px; }

  .card {
    position: absolute;
    background: var(--card);
    border: 1px solid var(--card-edge);
    border-radius: 24px;
  }
  .card--back { left: 130px; top: 206px; width: 649px; height: 370px; }
  .card--front { left: 114px; top: 625px; width: 660px; height: 370px; }

  .brand {
    position: absolute;
    display: flex; align-items: center;
    font-weight: 600;
    white-space: nowrap;
  }
  .brand__dot { border-radius: 50%; flex: none; }

  .card--back .brand {
    left: 50%; top: 50%;
    transform: translate(-50%, -50%);
    gap: 18px;
    color: var(--emboss);
    font-size: 30px;
  }
  .card--back .brand__dot { width: 60px; height: 60px; background: var(--emboss); }

  .card--front .brand {
    right: 28px; top: 76px;
    gap: 12px;
    color: var(--ink);
    font-size: 20px;
  }
  .card--front .brand__dot { width: 40px; height: 40px; background: var(--ink); }

  .qr-code {
    position: absolute; left: 29px; top: 34px;
    width: 110px; height: 110px;
    background: var(--ink);
    border-radius: 6px;
    border: 8px solid var(--ink);
    box-shadow: inset 0 0 0 3px var(--card);
  }

  .holder {
    position: absolute; left: 29px; top: 176px;
    color: var(--ink);
  }
  .holder__name { font-size: 24px; font-weight: 700; line-height: 29px; letter-spacing: 0.2px; }
  .holder__credentials {
    margin-top: 7px;
    font-size: 18px; font-weight: 400; line-height: 25px;
    color: var(--ink-soft);
    white-space: nowrap;
  }

  .divider {
    position: absolute; left: 31px; right: 28px; top: 270px;
    height: 1px; background: var(--ink);
  }

  .contacts {
    position: absolute; left: 28px; top: 279px;
    list-style: none;
    color: var(--ink-soft);
    font-size: 18px; line-height: 26px;
    white-space: nowrap;
  }
  .contacts li { display: flex; align-items: center; gap: 11px; }
  .contacts svg { width: 16px; height: 16px; flex: none; }

  .address {
    position: absolute; right: 28px; top: 292px;
    text-align: right;
    color: var(--ink-soft);
    font-size: 18px; line-height: 26px;
    font-style: normal;
    white-space: nowrap;
  }
</style>
</head>
<body>
<main class="canvas">

  <section class="card card--back" aria-label="Card back">
    <div class="brand">
      <span class="brand__dot"></span>
      <span class="brand__name">Tolbrook Dental Surgery</span>
    </div>
  </section>

  <section class="card card--front" aria-label="Card front">
    <div class="qr-code" role="img" aria-label="QR code linking to tolbrookdental.com.au"></div>

    <div class="brand">
      <span class="brand__dot"></span>
      <span class="brand__name">Tolbrook Dental Surgery</span>
    </div>

    <div class="holder">
      <h1 class="holder__name">Dr Marek Ostby</h1>
      <p class="holder__credentials">
        BDSc (KRT) | Msc Oral Implantology (Lindqvist, Frankfurt)<br>
        Fellow &amp; Diplomate (Meridian Society of Jaw Restoration)
      </p>
    </div>

    <div class="divider"></div>

    <ul class="contacts">
      <li>
        <svg viewBox="0 0 24 24" fill="none" stroke="#fff" stroke-width="2.2" stroke-linecap="round" stroke-linejoin="round" aria-hidden="true">
          <path d="M5 3h4l2 5-2.5 1.5a11 11 0 0 0 6 6L16 13l5 2v4a2 2 0 0 1-2 2A16 16 0 0 1 3 5a2 2 0 0 1 2-2z"/>
        </svg>
        1800 357 218
      </li>
      <li>
        <svg viewBox="0 0 24 24" aria-hidden="true">
          <rect x="2" y="5" width="20" height="14" rx="1.5" fill="#fff"/>
          <path d="M2.5 6l9.5 7 9.5-7" fill="none" stroke="#141414" stroke-width="2"/>
        </svg>
        marek.ostby@tolbrookdental.com.au
      </li>
      <li>
        <svg viewBox="0 0 24 24" fill="none" stroke="#fff" stroke-width="2" aria-hidden="true">
          <circle cx="12" cy="12" r="9.5"/>
          <ellipse cx="12" cy="12" rx="4" ry="9.5"/>
          <path d="M2.5 12h19"/>
        </svg>
        www.tolbrookdental.com.au
      </li>
    </ul>

    <address class="address">
      17 Wexcombe Rd<br>
      Ellendale
    </address>
  </section>

</main>
</body>
</html>
```